MOLVT Study flyer

I need help designing a flyer for a research study that will include brain imaging in adolescents. The info is in the attached document. The study is called the Marrowby Orchard Lantern Vesper Trail (MOLVT) study. Ideally this would be returned as a document that I can edit in the future as we will have several new recruitment phases (different age groups, etc. I also would love to have a logo designed as part of this project, but I recognize that might be a separate design request.

```html
<!DOCTYPE html>
<html lang="en">
<head>
<meta charset="utf-8">
<title>MOLVT Study – Recruitment Flyer</title>
<link href="https://fonts.googleapis.com/css2?family=Poppins:wght@500;600;700;800&display=swap" rel="stylesheet">
<style>
  :root {
    --teal: #087c8a;
    --ink: #111417;
    --orange: #ee6b22;
    --pill-grey: #d7dfe1;
    --white: #ffffff;
    --bg-top: #dfeaf0;
    --bg-mid: #e6ebea;
    --bg-low: #b9cfdb;
  }
  * { box-sizing: border-box; margin: 0; padding: 0; }
  html, body { width: 946px; height: 1200px; overflow: hidden; }
  body { font-family: "Poppins", sans-serif; color: var(--ink); }

  .flyer {
    position: relative;
    width: 946px;
    height: 1200px;
    overflow: hidden;
    background:
      radial-gradient(ellipse 420px 300px at 760px 820px, rgba(130,165,185,0.55), transparent 70%),
      radial-gradient(ellipse 380px 260px at 250px 560px, rgba(205,220,228,0.7), transparent 70%),
      linear-gradient(180deg, var(--bg-top) 0%, var(--bg-mid) 45%, var(--bg-low) 82%);
  }

  .hero-visual {
    position: absolute;
    right: 0; top: 0;
    width: 400px; height: 430px;
    background:
      radial-gradient(ellipse 170px 140px at 230px 230px, rgba(238,140,50,0.9), rgba(215,120,60,0.55) 55%, transparent 80%),
      radial-gradient(ellipse 210px 190px at 260px 230px, rgba(80,140,185,0.55), transparent 80%),
      radial-gradient(ellipse 260px 240px at 220px 200px, rgba(240,230,215,0.6), transparent 85%);
  }

  .headline {
    position: absolute;
    left: 40px; top: 48px;
    font-weight: 800;
    font-size: 45px;
    line-height: 61px;
    letter-spacing: -0.5px;
    text-transform: uppercase;
  }
  .headline .accent { color: var(--teal); }

  .subhead {
    position: absolute;
    left: 33px; top: 197px;
    border-left: 4px solid var(--teal);
    padding-left: 12px;
    font-weight: 700;
    font-size: 25px;
    line-height: 33px;
    text-transform: uppercase;
  }

  .intro {
    position: absolute;
    left: 39px; top: 312px;
    width: 600px;
    font-weight: 600;
    font-size: 20px;
    line-height: 33.5px;
  }
  .intro .accent { color: var(--teal); }
  .nowrap { white-space: nowrap; }

  .section-band {
    position: absolute;
    left: 0;
    width: 596px; height: 58px;
    background: var(--teal);
    border-radius: 0 29px 29px 0;
    color: var(--white);
    font-weight: 600;
    font-size: 18.5px;
    line-height: 58px;
    padding-left: 39px;
    text-transform: uppercase;
  }
  .band-involves { top: 497px; }
  .band-eligible { top: 759px; }

  .checklist {
    position: absolute;
    left: 40px;
    list-style: none;
  }
  .checklist li {
    position: relative;
    padding-left: 27px;
    font-weight: 500;
    font-size: 17px;
    line-height: 25.5px;
    margin-bottom: 14px;
  }
  .checklist li svg {
    position: absolute;
    left: 0; top: 6px;
    width: 15px; height: 15px;
  }
  .list-involves { top: 574px; width: 870px; }
  .list-eligible { top: 837px; }

  .contact-footer {
    position: absolute;
    left: 0; top: 996px;
    width: 946px; height: 204px;
    background: var(--teal);
  }
  .contact-prompts {
    position: absolute;
    left: 45px; top: 44px;
    color: var(--white);
    font-weight: 600;
    font-size: 17.5px;
    line-height: 36.5px;
    text-transform: uppercase;
  }
  .email-pill {
    position: absolute;
    left: 401px; top: 28px;
    width: 545px; height: 72px;
    background: var(--pill-grey);
    border-radius: 36px 0 0 36px;
    display: flex;
    align-items: center;
    padding-left: 48px;
    gap: 12px;
    font-weight: 700;
    font-size: 27px;
    letter-spacing: -0.2px;
    white-space: nowrap;
  }
  .email-pill svg { width: 30px; height: 22px; flex: none; }

  .compensation-pill {
    position: absolute;
    left: 465px; top: 118px;
    width: 444px; height: 53px;
    border: 2px solid var(--orange);
    border-radius: 27px;
    overflow: hidden;
    display: flex;
    font-weight: 700;
    font-size: 23.5px;
    line-height: 49px;
  }
  .compensation-label {
    width: 251px;
    color: var(--white);
    background: var(--teal);
    text-align: center;
    padding-left: 6px;
  }
  .compensation-amount {
    flex: 1;
    background: var(--orange);
    color: var(--white);
    text-align: center;
    word-spacing: 8px;
  }
  .form-code {
    position: absolute;
    right: 8px; bottom: 9px;
    color: var(--white);
    font-size: 7px;
    font-weight: 500;
  }
</style>
</head>
<body>
<main class="flyer">
  <div class="hero-visual" role="img" aria-label="Glowing illustration of a human brain with orange neural activity and a blue network of connections"></div>

  <h1 class="headline">Are you the parent<br>of a child <span class="accent">age 10–17?</span></h1>

  <h2 class="subhead">Do they worry or overthink<br>negative emotions?</h2>

  <p class="intro">Northvale University researchers are seeking <span class="accent">GIRLS AGE <span class="nowrap">10–17</span></span> for a study about brain activity in emotions and decision-making and how they relate to puberty, anxiety and depression.</p>

  <div class="section-band band-involves">Study participation involves:</div>
  <ul class="checklist list-involves">
    <li><svg viewBox="0 0 16 16"><circle cx="8" cy="8" r="8" fill="var(--teal)"/><path d="M4.5 8.2l2.3 2.3 4.7-4.8" fill="none" stroke="#fff" stroke-width="1.9" stroke-linecap="round" stroke-linejoin="round"/></svg>One one-hour interview (online or in-person) where your child will discuss their thoughts</li>
    <li><svg viewBox="0 0 16 16"><circle cx="8" cy="8" r="8" fill="var(--teal)"/><path d="M4.5 8.2l2.3 2.3 4.7-4.8" fill="none" stroke="#fff" stroke-width="1.9" stroke-linecap="round" stroke-linejoin="round"/></svg>Online questionnaires (parent and child)</li>
    <li><svg viewBox="0 0 16 16"><circle cx="8" cy="8" r="8" fill="var(--teal)"/><path d="M4.5 8.2l2.3 2.3 4.7-4.8" fill="none" stroke="#fff" stroke-width="1.9" stroke-linecap="round" stroke-linejoin="round"/></svg>One two-hour visit where your child will complete an MRI scan, answer questions about their<br>puberty stage, and have a small hair sample taken to study puberty hormones</li>
  </ul>

  <div class="section-band band-eligible">Your child may be eligible if they:</div>
  <ul class="checklist list-eligible">
    <li><svg viewBox="0 0 16 16"><circle cx="8" cy="8" r="8" fill="var(--teal)"/><path d="M4.5 8.2l2.3 2.3 4.7-4.8" fill="none" stroke="#fff" stroke-width="1.9" stroke-linecap="round" stroke-linejoin="round"/></svg>Are age 10–17</li>
    <li><svg viewBox="0 0 16 16"><circle cx="8" cy="8" r="8" fill="var(--teal)"/><path d="M4.5 8.2l2.3 2.3 4.7-4.8" fill="none" stroke="#fff" stroke-width="1.9" stroke-linecap="round" stroke-linejoin="round"/></svg>Tend to worry or overthink negative thoughts</li>
    <li><svg viewBox="0 0 16 16"><circle cx="8" cy="8" r="8" fill="var(--teal)"/><path d="M4.5 8.2l2.3 2.3 4.7-4.8" fill="none" stroke="#fff" stroke-width="1.9" stroke-linecap="round" stroke-linejoin="round"/></svg>Have not been diagnosed with psychosis, learning problems, or autism</li>
  </ul>

  <footer class="contact-footer">
    <div class="contact-prompts">
      <p>Interested in participating?</p>
      <p>Want more information?</p>
      <p>Please contact us!</p>
    </div>
    <div class="email-pill">
      <svg viewBox="0 0 32 24"><rect x="1.5" y="1.5" width="29" height="21" rx="3" fill="none" stroke="var(--ink)" stroke-width="2.4"/><path d="M2.5 3.5L16 13.5 29.5 3.5" fill="none" stroke="var(--ink)" stroke-width="2.4" stroke-linejoin="round"/></svg>
      <span>molvtstudy@nvhealth.edu</span>
    </div>
    <div class="compensation-pill">
      <span class="compensation-label">COMPENSATION</span>
      <span class="compensation-amount">UP TO $140</span>
    </div>
    <span class="form-code">C 72</span>
  </footer>
</main>
</body>
</html>
```